Verdant Banner Design

We need 3 Banners for our superfood supplement e-commerce store.

1. Banner that advertises the food combining chart Dimensions 417 × 464 https://verdantlift.com/content/11-food-combining-rules

2. We need a banner that advertises our subscription program. (Dimensions 388 × 219)

3. We need a banner that highlights our ingredients. (Dimensions 388 × 215)

Our website: https://verdantlift.com/

1. The sizes are in dimensions.

2. Yes the banners are for our website, replacing the ones on the front page now https://verdantlift.com/

Content of Banners

1. Advertisng the food combining chart.

2. Advertising our Subscription program.

3 Advertising our ingredients.

Just use words like:

"Combine the right foods"

Target Market(s)

Organic Superfood Supplement

Contact Information for Business Card

The Business card has to be double sided and must have our logo

Colors

Designer to choose colors to be used in the design.

Requirements
Must have
• 1. You can use the attached images or not, it is up to you, please be creative.
• 2. Please provide the Raw AI files, and also give it in the following formats: JPEG, PNG,
• 3. I have added a file in the brief called subscription image please use to get an idea of the type of banner we are looking for, of course using our product images
Nice to have
• 1. Please show business card design as well, this will help us decide to choose you.
• 2. Please read the ingredients on the product itself, and if you can use some images for the ingredient banner that would be good.
• 3. The business card should have the following:
• Name: Brent Halloway
• Title: Co-Founder
• Address: Baldwin, NY
• Logo (see attached)
• Phone #: 877-555-0143
• Mobile #: 917-555-0188
• Email: info@verdantlift.com
• Website: www.verdantlift.com
Should not have
• No meat or dairy products in your images

```html
<!DOCTYPE html>
<html lang="en">
<head>
<meta charset="utf-8">
<title>Verdant Lift Banners</title>
<link rel="stylesheet" href="https://fonts.googleapis.com/css2?family=Oswald:wght@400;500&family=Arimo:wght@400;700&display=swap">
<style>
  :root {
    --page: #ffffff;
    --card: #fffdf5;
    --card-edge: #e4e1d6;
    --ribbon: #ff5333;
    --ribbon-notch: #fffdf5;
    --head-cell: #fddccc;
    --grid-line: #ee7585;
    --good: #92d050;
    --fair: #ffff00;
    --poor-red: #ff0000;
    --ink: #111111;
    --white: #ffffff;
    --promo-bg: #1d1d1d;
    --promo-edge: #d9d9d9;
    --brand: #8cc63f;
  }
  * { box-sizing: border-box; margin: 0; padding: 0; }
  html, body { width: 1200px; height: 1200px; overflow: hidden; background: var(--page); }
  body { position: relative; font-family: "Arimo", Arial, sans-serif; color: var(--ink); }

  /* Chart banner */
  .chart-banner {
    position: absolute; left: 258px; top: 50px; width: 624px; height: 694px;
    background: var(--card); border: 1px solid var(--card-edge);
  }
  .chart-banner .ribbon {
    position: absolute; left: 11px; top: 10px; width: 600px; height: 98px;
  }
  .chart-banner .ribbon svg { position: absolute; inset: 0; }
  .chart-banner .ribbon-title {
    position: absolute; inset: 0; display: flex; align-items: center; justify-content: center;
    font-family: "Oswald", "Arial Narrow", sans-serif; font-weight: 400; font-size: 39px;
    letter-spacing: 1px; color: var(--white); padding-bottom: 4px;
  }
  .produce-photo {
    position: absolute; left: 11px; top: 127px; width: 600px; height: 198px;
    background:
      radial-gradient(ellipse at 15% 40%, #9b2335 0 18%, transparent 30%),
      radial-gradient(ellipse at 30% 55%, #f2c81f 0 14%, transparent 26%),
      radial-gradient(ellipse at 47% 45%, #f59a1c 0 12%, transparent 24%),
      radial-gradient(ellipse at 65% 50%, #5fae2e 0 18%, transparent 30%),
      radial-gradient(ellipse at 85% 45%, #f4b400 0 14%, transparent 26%),
      linear-gradient(180deg, #ffffff 0%, #f2e7c9 45%, #c85a2c 100%);
  }

  .combo-table {
    position: absolute; left: 11px; top: 337px; width: 600px;
    border-collapse: collapse; table-layout: fixed;
  }
  .combo-table th, .combo-table td {
    border: 1.5px solid var(--grid-line); height: 45px; padding: 0;
  }
  .combo-table th {
    background: var(--head-cell); text-align: left; vertical-align: top;
    font-weight: 400; font-size: 13px; line-height: 16px; padding: 4px 6px;
  }
  .combo-table th.corner { font-size: 20px; font-weight: 700; vertical-align: middle; padding: 0 10px; }
  .combo-table th.row-label { font-size: 13px; vertical-align: middle; padding: 0 10px; }
  .combo-table col.label-col { width: 211px; }
  .cell-good { background: var(--good); }
  .cell-fair { background: var(--fair); }
  .cell-poor { background: var(--poor-red); }

  .legend {
    position: absolute; left: 11px; top: 626px; height: 36px;
    display: flex; align-items: center; font-size: 18px;
  }
  .legend .swatch { width: 36px; height: 36px; margin-right: 15px; }
  .legend .label { margin-right: 115px; width: 40px; }

  /* Discount banner */
  .promo-banner {
    position: absolute; left: 276px; top: 797px; width: 581px; height: 327px;
    background: linear-gradient(90deg, #1b1b1b 0%, #242222 50%, #1b1b1b 100%);
    border: 1px solid var(--promo-edge); overflow: hidden;
  }
  .brand-name {
    position: absolute; left: 24px; top: 28px;
    display: flex; align-items: center; gap: 10px;
    font-family: "Arimo", Arial, sans-serif; font-weight: 700; font-size: 34px; color: var(--brand);
  }
  .brand-name .mark { width: 20px; height: 20px; background: var(--brand); }
  .fruit-photo {
    position: absolute; left: 246px; top: -2px; width: 248px; height: 155px;
    border: 3px solid var(--white); border-top: none; border-radius: 0 0 30px 30px;
    background:
      radial-gradient(ellipse at 20% 30%, #6d1d3a 0 22%, transparent 34%),
      radial-gradient(ellipse at 70% 45%, #f2c81f 0 20%, transparent 32%),
      radial-gradient(ellipse at 30% 85%, #3f8a2a 0 20%, transparent 32%),
      linear-gradient(135deg, #8a2430, #e88a3c 55%, #d9564a);
  }
  .veg-photo {
    position: absolute; left: 326px; top: 172px; width: 248px; height: 158px;
    border: 3px solid var(--white); border-bottom: none; border-radius: 30px 30px 0 0;
    background:
      radial-gradient(ellipse at 70% 20%, #d22a1e 0 20%, transparent 32%),
      radial-gradient(ellipse at 20% 60%, #b8c33a 0 18%, transparent 30%),
      radial-gradient(ellipse at 75% 75%, #4f9a2c 0 24%, transparent 36%),
      linear-gradient(160deg, #7a3b22, #3e6d25 60%, #6a9c34);
  }
  .discount {
    position: absolute; left: 16px; top: 182px; display: flex; align-items: center;
  }
  .discount .amount {
    font-family: "Arimo", Arial, sans-serif; font-size: 128px; line-height: 1; color: var(--white);
    letter-spacing: -6px;
  }
  .discount .tag {
    margin-left: -10px; margin-top: 4px; height: 48px; width: 202px;
    background: var(--white); border-radius: 24px;
    display: flex; align-items: center;
  }
  .discount .percent {
    width: 42px; height: 42px; margin-left: 3px; border-radius: 50%;
    background: var(--promo-bg); color: var(--white);
    display: flex; align-items: center; justify-content: center; font-size: 24px;
  }
  .discount .word { margin-left: 12px; font-size: 25px; color: var(--ink); letter-spacing: 0.5px; }
</style>
</head>
<body>

<section class="chart-banner">
  <div class="ribbon">
    <svg width="600" height="98" viewBox="0 0 600 98">
      <polygon points="0,0 600,0 575,49 600,98 0,98 25,49" fill="var(--ribbon)"/>
    </svg>
    <div class="ribbon-title">FOOD COMBINING CHART</div>
  </div>

  <div class="produce-photo" role="img" aria-label="Row of fresh fruit and vegetables: grapes, bananas, oranges, lettuce, peppers and apples"></div>

  <table class="combo-table">
    <colgroup>
      <col class="label-col"><col><col><col><col><col>
    </colgroup>
    <tr>
      <th class="corner">Food Categories</th>
      <th>Vegetab-<br>les</th>
      <th>Fats</th>
      <th>Starches</th>
      <th>Sweet<br>Fruits</th>
      <th>Low Acid<br>Fruits</th>
    </tr>
    <tr>
      <th class="row-label">Vegetables</th>
      <td class="cell-good"></td><td class="cell-poor"></td><td class="cell-good"></td><td class="cell-poor"></td><td class="cell-good"></td>
    </tr>
    <tr>
      <th class="row-label">Fats</th>
      <td class="cell-fair"></td><td class="cell-good"></td><td class="cell-good"></td><td class="cell-good"></td><td class="cell-poor"></td>
    </tr>
    <tr>
      <th class="row-label">Starches</th>
      <td class="cell-good"></td><td class="cell-good"></td><td class="cell-fair"></td><td class="cell-good"></td><td class="cell-good"></td>
    </tr>
    <tr>
      <th class="row-label">Sweet Fruits</th>
      <td class="cell-good"></td><td class="cell-poor"></td><td class="cell-good"></td><td class="cell-good"></td><td class="cell-fair"></td>
    </tr>
    <tr>
      <th class="row-label">Low Acid Fruits</th>
      <td class="cell-fair"></td><td class="cell-good"></td><td class="cell-fair"></td><td class="cell-good"></td><td class="cell-poor"></td>
    </tr>
  </table>

  <div class="legend">
    <span class="swatch cell-good"></span><span class="label">GOOD</span>
    <span class="swatch cell-fair"></span><span class="label">FAIR</span>
    <span class="swatch cell-good"></span><span class="label">POOR</span>
  </div>
</section>

<section class="promo-banner">
  <div class="brand-name"><span class="mark"></span>Verdant Lift</div>
  <div class="fruit-photo" role="img" aria-label="Fresh fruit: grapes, orange, banana, grapefruit and cucumber"></div>
  <div class="veg-photo" role="img" aria-label="Market vegetables: tomatoes, apples, green beans and potatoes"></div>
  <div class="discount">
    <span class="amount">30</span>
    <span class="tag"><span class="percent">%</span><span class="word">DISCOUNT</span></span>
  </div>
</section>

</body>
</html>
```